Business Card Design and Basic Text Logo

We are looking for a business card design for an e-business company. Our business is the parent company of a few website businesses. The final logo and business card design will communicate a conservative but modern and expansive business

The Logo text is: 87Merchant
We would also like a basic text logo design for 87Merchant. The logo could also fill up the reverse side of the business card.

The colours we would like to use are:
White
Navy
Black

This is the text that will be added to the card:

Dean Colley
Business Development Manager

Phone: +61 417 658 294
Email: dean.colley@87merchant.com.au

Industry/Entity Type

Business

Logo Text

87Merchant

Logo styles of interest
Pictorial/Combination Logo
Requirements
Must have
• Modern and attractive design
Nice to have
• communicate a conservative but modern and expansive business
Should not have
• Should be too dull and plan
• But also should be overly colourful

```html
<!DOCTYPE html>
<html lang="en">
<head>
<meta charset="utf-8">
<title>87Merchant Stationery</title>
<link href="https://fonts.googleapis.com/css2?family=PT+Sans+Narrow:wght@400;700&display=swap" rel="stylesheet">
<style>
  :root {
    --board: #ebebeb;
    --ink: #111111;
    --charcoal: #333333;
    --weave-dark: #141414;
    --weave-mid: #2c2c2c;
    --navy: #060626;
    --white: #ffffff;
    --silver: #e6e6e6;
    --black: #000000;
  }
  * { margin: 0; padding: 0; box-sizing: border-box; }
  html, body { width: 1200px; height: 1000px; overflow: hidden; }
  body {
    background: var(--board);
    font-family: "PT Sans Narrow", "Arial Narrow", sans-serif;
    position: relative;
    color: var(--ink);
  }
  .section-label {
    position: absolute;
    font-size: 34px;
    font-weight: 400;
    color: var(--ink);
    text-align: center;
    letter-spacing: 0.5px;
  }
  .weave {
    position: absolute;
    background: linear-gradient(135deg, var(--weave-mid), var(--weave-dark) 60%, var(--weave-mid));
  }
  .wordmark {
    position: absolute;
    display: flex;
    align-items: center;
    gap: 12px;
    color: var(--silver);
    white-space: nowrap;
  }
  .wordmark-dot {
    border-radius: 50%;
    background: currentColor;
    flex: none;
  }
  .squares-h {
    position: absolute;
    background: repeating-linear-gradient(90deg, var(--navy) 0 26px, var(--white) 26px 52.6px);
  }

  /* Letterhead */
  .letterhead {
    position: absolute; left: 36px; top: 56px; width: 646px; height: 914px;
    background: var(--white);
    box-shadow: 0 2px 6px rgba(0,0,0,0.45);
  }
  .letterhead-header { left: 0; top: 0; width: 646px; height: 107px; }
  .letterhead .wordmark { left: 18px; top: 28px; font-size: 40px; }
  .letterhead .wordmark-dot { width: 44px; height: 44px; }
  .letterhead-sender {
    position: absolute; left: 358px; top: 32px;
    color: var(--white); line-height: 20px;
  }
  .letterhead-sender .name { font-size: 20px; }
  .letterhead-sender .role { font-size: 19px; }
  .letterhead .squares-top { left: 20px; top: 109px; width: 604px; height: 33px; }
  .letterhead .squares-bottom { left: 20px; top: 833px; width: 604px; height: 33px; }
  .letterhead-footer {
    position: absolute; left: 0; bottom: 0; width: 646px; height: 48px;
    background: var(--black); color: var(--white);
    font-size: 21px;
  }
  .contact { position: absolute; display: flex; align-items: center; gap: 6px; white-space: nowrap; }
  .letterhead-footer .phone { left: 72px; top: 10px; }
  .letterhead-footer .email { left: 292px; top: 10px; gap: 10px; }

  /* Logo */
  .logo-display { left: 742px; top: 112px; color: var(--charcoal); font-size: 72px; gap: 18px; }
  .logo-display .wordmark-dot { width: 80px; height: 80px; }

  /* Business cards */
  .card {
    position: absolute; width: 411px; background: var(--white);
    box-shadow: 0 2px 6px rgba(0,0,0,0.45); overflow: hidden;
  }
  .card-front { left: 727px; top: 388px; height: 264px; }
  .card-front .weave { left: 0; top: 0; width: 411px; height: 249px; }
  .card-front .squares-h {
    left: 0; top: 250px; width: 411px; height: 14px;
    background: repeating-linear-gradient(90deg, var(--navy) 0 22px, var(--white) 22px 43px);
  }
  .card-front .wordmark { left: 76px; top: 108px; font-size: 42px; }
  .card-front .wordmark-dot { width: 48px; height: 48px; }

  .card-back { left: 727px; top: 707px; height: 263px; }
  .squares-v {
    position: absolute; top: 0; width: 15px; height: 236px;
    background: repeating-linear-gradient(180deg, var(--white) 0 12px, var(--navy) 12px 28px);
  }
  .squares-v.left { left: 0; }
  .squares-v.right { right: 0; }
  .card-back .weave { left: 15px; top: 0; width: 381px; height: 236px; }
  .card-back .wordmark { left: 64px; top: 62px; font-size: 42px; }
  .card-back .wordmark-dot { width: 48px; height: 48px; }
  .card-back-sender {
    position: absolute; left: 15px; top: 160px; width: 381px;
    text-align: center; color: var(--white); line-height: 19px;
  }
  .card-back-sender .name { font-size: 20px; }
  .card-back-sender .role { font-size: 17px; }
  .card-back-contacts {
    position: absolute; left: 0; top: 241px; width: 411px; height: 22px;
    color: var(--navy); font-size: 15px;
  }
  .card-back-contacts .phone { left: 18px; top: 2px; gap: 3px; }
  .card-back-contacts .email { right: 16px; top: 2px; gap: 4px; }
</style>
</head>
<body>

  <h2 class="section-label" style="left:240px; top:8px; width:200px;">LETTERHEAD</h2>
  <h2 class="section-label" style="left:832px; top:48px; width:200px;">LOGO</h2>
  <h2 class="section-label" style="left:782px; top:322px; width:300px;">BUSINESS CARDS</h2>

  <!-- Letterhead -->
  <section class="letterhead">
    <div class="weave letterhead-header" role="img" aria-label="Dark charcoal woven texture band"></div>
    <div class="wordmark"><span class="wordmark-dot"></span><span>87MERCHANT</span></div>
    <div class="letterhead-sender">
      <div class="name">DEAN COLLEY</div>
      <div class="role">BUSINESS DEVELOPMENT MANAGER</div>
    </div>
    <div class="squares-h squares-top"></div>
    <div class="squares-h squares-bottom"></div>
    <footer class="letterhead-footer">
      <div class="contact phone">
        <svg width="20" height="28" viewBox="0 0 20 28" aria-hidden="true"><path d="M5 2 L9 2 L10 8 L7 10 Q8 16 12 20 L15 17 L19 20 L18 25 Q12 27 7 20 Q2 12 5 2 Z" fill="var(--white)"/></svg>
        <span>+61 417 658 294</span>
      </div>
      <div class="contact email">
        <svg width="32" height="22" viewBox="0 0 32 22" aria-hidden="true"><rect x="0" y="0" width="32" height="22" fill="var(--white)"/><path d="M1 1 L16 13 L31 1" stroke="var(--black)" stroke-width="2.5" fill="none"/></svg>
        <span>dean.colley@87merchant.com.au</span>
      </div>
    </footer>
  </section>

  <!-- Logo -->
  <div class="wordmark logo-display"><span class="wordmark-dot"></span><span>87MERCHANT</span></div>

  <!-- Business card front -->
  <section class="card card-front">
    <div class="weave" role="img" aria-label="Dark charcoal woven texture background"></div>
    <div class="wordmark"><span class="wordmark-dot"></span><span>87MERCHANT</span></div>
    <div class="squares-h"></div>
  </section>

  <!-- Business card back -->
  <section class="card card-back">
    <div class="squares-v left"></div>
    <div class="weave" role="img" aria-label="Dark charcoal woven texture background"></div>
    <div class="squares-v right"></div>
    <div class="wordmark"><span class="wordmark-dot"></span><span>87MERCHANT</span></div>
    <div class="card-back-sender">
      <div class="name">DEAN COLLEY</div>
      <div class="role">BUSINESS DEVELOPMENT MANAGER</div>
    </div>
    <div class="card-back-contacts">
      <div class="contact phone">
        <svg width="12" height="16" viewBox="0 0 20 28" aria-hidden="true"><path d="M5 2 L9 2 L10 8 L7 10 Q8 16 12 20 L15 17 L19 20 L18 25 Q12 27 7 20 Q2 12 5 2 Z" fill="var(--navy)"/></svg>
        <span>+61 417 658 294</span>
      </div>
      <div class="contact email">
        <svg width="15" height="11" viewBox="0 0 32 22" aria-hidden="true"><rect x="0" y="0" width="32" height="22" fill="var(--navy)"/><path d="M1 1 L16 13 L31 1" stroke="var(--white)" stroke-width="3" fill="none"/></svg>
        <span>dean.colley@87merchant.com.au</span>
      </div>
    </div>
  </section>

</body>
</html>
```